Commercial Real Estate Company Needs an Awesome Flyer Design for their Oceanfront Property

We need a 2-page flyer or our Class A Oceanfront Property in Santa Monica, California. Approximately 16,149 square feet of Class A rare oceanfront office space with private balconies will be in available 4th Quarter of 2014. The SPACE has not been on the market for over 20 YEARS!

I attached our Previous 2-page flyer for the 2,353 square feet. We need a new vibrant, modern flyer that will attract Tech, Entertainment, Financial, and Marketing Companies to our building. Also, the 2nd Floor Space Plan is attached.

Also, please check out our website www.velabrookproperties.com. We would like to use the colors of our website and logo to incorporate with the flyer.

I updated the Must Have's on the Listing!

Target Market(s)

Entertainment, Financial, Tech Companies

Industry/Entity Type

Real Estate

Requirements
Must have
• Our Company Logo, Company, Leasing Agents On the First and 2nd Page

Dustin R. Hallorann (310) 555-0142
dusty@velabrookproperties.com

Owen Tu (310) 555-0187
owen@velabrookproperties.com

Velabrook Properties.
5172 E Harlow Ave, Suite 414
West Hollywood, Ca. 90069
(310) 555-0142
www.velabrookproperties.com

Also, the Front Page should indicate

"Rare Class A Oceanfront Office Space in the heart of Santa Monica"
"2nd Floor Office Space consisting of 16,159 square feet with private balconies."
Nice to have
• Please use description of the office building. You can omit whatever you think is unnecessary

"Bellwether Court is one of Santa Monica's rare commercial properties that is both strategically located in the city's burgeoning central business district, yet ideally positioned on palm-lined Ocean Ave directly across from the Pacific Ocean. Built in 1987, the 3-story mixed-use commercial and retail property features prestigious retail Tenants such as Kelp Haus and Tidal Oven."

"A year-round coastal Mediterranean climate, a highly diverse business sector, and the vibrant, pedestrian-oriented Linden Row Arcade and Marigold Commons makes this beachside community a highly desirable commercial and retail location."

```html
<!DOCTYPE html>
<html lang="en">
<head>
<meta charset="utf-8">
<title>Bellwether Court – Leasing Flyer</title>
<link rel="stylesheet" href="https://fonts.googleapis.com/css2?family=Montserrat:wght@500;600;700&family=Ubuntu:wght@400;500&family=Tangerine:wght@400&display=swap">
<style>
:root{
  --yellow:#f3c01c;
  --yellow-light:#fbe48a;
  --ink:#2b2b2b;
  --blue:#1f6db4;
  --navy:#2c3a8f;
  --grey-panel:#e4e4e6;
  --grey-text:#555;
  --script:#8a8a8a;
  --page:#f7f7f7;
  --backdrop:#e9e9eb;
}
*{margin:0;padding:0;box-sizing:border-box}
html,body{width:1200px;height:835px;overflow:hidden;background:var(--backdrop)}
body{position:relative;font-family:"Ubuntu",Arial,sans-serif;color:var(--ink)}
.page{position:absolute;top:30px;width:548px;height:773px;background:var(--page);overflow:hidden}
.page--front{left:30px}
.page--back{left:618px}
.abs{position:absolute}
.photo{position:absolute}

/* front header */
.header-swoosh{left:0;top:0}
.title{left:24px;top:26px;font-family:"Montserrat",sans-serif;font-weight:700;font-size:25px;letter-spacing:1px;color:var(--ink)}
.title-address{left:60px;top:56px;font-family:"Montserrat",sans-serif;font-weight:600;font-size:17px;letter-spacing:1px;color:var(--ink)}
.brand{display:flex;flex-direction:column;align-items:center;gap:8px}
.brand-mark{width:46px;height:46px;border-radius:50%;background:var(--yellow)}
.brand-name{font-family:"Montserrat",sans-serif;font-weight:600;font-size:12px;letter-spacing:3px;color:var(--ink);text-align:center;line-height:1.35}
.tagline{left:35px;top:108px;font-size:15px;line-height:19px;color:var(--blue);font-weight:500;z-index:2}

.hero-photo{left:0;top:154px;width:548px;height:240px;background:linear-gradient(180deg,#3d6fc6 0%,#7ea6e0 35%,#eef1f6 60%,#c9ccd4 80%,#3a3f66 100%)}
.headline{left:0;width:548px;top:414px;text-align:center;font-size:15.5px;line-height:19px;color:var(--blue);font-weight:500}
.floorplan{left:11px;top:458px;width:178px;height:188px;background:#fff;border:1px solid #c9c9c9}
.description{left:200px;top:458px;width:190px;font-size:6.6px;line-height:8.8px;text-align:justify;color:#333}
.description p+p{margin-top:8px}
.balcony-photo{left:404px;top:446px;width:132px;height:200px;border-radius:50%;background:linear-gradient(180deg,#b9d6ee 0%,#dfe9ef 45%,#9fb28a 70%,#d9d2c2 100%)}

.contact-panel{background:var(--grey-panel);border-radius:18px;display:flex;gap:22px;padding:9px 14px 0 14px}
.contact{font-size:10px;line-height:15px;color:#333}
.contact-name{font-size:13px;font-weight:500;color:var(--navy);margin-bottom:3px;white-space:nowrap}
.contact-line{display:flex;align-items:center;gap:3px;white-space:nowrap}
.contact-line svg{flex:none}
.script{font-family:"Tangerine",cursive;color:var(--script)}
.script--front{left:416px;top:652px;font-size:36px;line-height:34px;z-index:2}

.footer{left:0;bottom:0;width:548px;height:52px}
.footer-phone{font-size:15px;font-weight:500;color:var(--ink);display:flex;align-items:center;gap:3px}
.footer-small{font-size:9.5px;color:#333;display:flex;align-items:center;gap:3px;white-space:nowrap}

/* back page */
.amenities{left:14px;top:20px;width:256px}
.amenities h2{font-size:14px;font-weight:500;color:var(--blue);margin-bottom:10px}
.amenities ul{list-style:none}
.amenities li{display:flex;gap:5px;font-size:7.2px;line-height:8.6px;color:#222;margin-bottom:9px}
.amenities li svg{flex:none;margin-top:1px}
.terrace-photo{left:277px;top:0;width:271px;height:198px;background:linear-gradient(180deg,#cfe0f0 0%,#e7ecef 40%,#8f8f88 75%,#5d5b56 100%)}
.lobby-photo{left:0;top:198px;width:548px;height:206px;background:linear-gradient(90deg,#dcdcdc 0%,#f1f1f1 40%,#e9e9e9 62%,#c8343a 63%,#c8343a 78%,#ededed 79%)}
.map{left:14px;top:424px;width:252px;height:184px;border-radius:14px;background:linear-gradient(135deg,#f3f0e6,#efe6b8)}
.beach-photo{left:279px;top:424px;width:253px;height:184px;border-radius:14px;background:linear-gradient(180deg,#c9dcee 0%,#6f8d5f 30%,#d8ccb0 55%,#a79b86 100%)}
.script--back{left:206px;top:612px;font-size:48px;line-height:50px}
</style>
</head>
<body>

<section class="page page--front">
  <svg class="abs header-swoosh" width="548" height="110" viewBox="0 0 548 110" aria-hidden="true">
    <defs>
      <linearGradient id="yellowFrontTop" x1="0" y1="0" x2="1" y2="0">
        <stop offset="0" stop-color="#f3c01c"/><stop offset="1" stop-color="#f9db62"/>
      </linearGradient>
    </defs>
    <path d="M0 0H440C400 40 300 78 150 84C90 86 40 90 0 98Z" fill="url(#yellowFrontTop)"/>
    <path d="M0 98C40 90 90 86 150 84C300 78 400 40 440 0H452C410 46 310 86 150 92C90 94 40 98 0 106Z" fill="#d8d8d8"/>
  </svg>
  <h1 class="abs title">BELLWETHER COURT</h1>
  <div class="abs title-address">2280 OCEAN AVENUE</div>

  <div class="abs brand" style="left:420px;top:22px;width:116px">
    <span class="brand-mark"></span>
    <span class="brand-name">VELABROOK<br>PROPERTIES</span>
  </div>

  <p class="abs tagline">Rare “Class A” Oceanfront Office Space<br>in the heart of Santa Monica</p>

  <div class="photo hero-photo" role="img" aria-label="Photo of the white three-storey building on a sunny day with palm trees and street-level restaurants"></div>
  <svg class="abs" style="left:0;top:370px" width="548" height="40" viewBox="0 0 548 40" aria-hidden="true">
    <path d="M0 24C150 8 400 6 548 14V40H0Z" fill="var(--page)"/>
    <path d="M0 24C150 8 400 6 548 14V18C400 12 150 14 0 30Z" fill="#2c2c2c"/>
  </svg>

  <h2 class="abs headline">2nd Floor Office Space consisting of 16,159 square feet (divisible)<br>with Private Balconies and Patios.</h2>

  <div class="abs floorplan" role="img" aria-label="Second floor space plan showing divisible office suites"></div>

  <div class="abs description">
    <p>Bellwether Court is one of Santa Monica's rare commercial Office and Retail properties that is both strategically located within the City's burgeoning central business district; walking distance to the Promenade, Santa Monica Outdoor Mall, Pier and many other dining and shopping amenities; yet ideally positioned on the palm lined Ocean Avenue directly across the street from the Pacific Ocean. Built in 1987, the 3 story mix use commercial and retail property features prestigious retail tenants such as: Kelp Haus, Tidal Oven and Ember Counter.</p>
    <p>Santa Monica offers a year-round costal Mediterranean climate, a highly diverse business sector, and vibrant pedestrian-oriented Linden Row Arcade and the Marigold Commons makes this beachside community a highly desirable location. Santa Monica is home to many globally known professional, entertainment, and technology companies, in part due to the large talent pool that prefers to enjoy the beach lifestyle and the surrounding amenities.</p>
  </div>

  <div class="abs balcony-photo" role="img" aria-label="Photo of a planted balcony walkway overlooking the ocean and palms"></div>

  <div class="abs contact-panel" style="left:26px;top:664px;width:368px;height:66px">
    <div class="contact">
      <div class="contact-name">Dustin R. Hallorann</div>
      <div class="contact-line"><svg width="10" height="10" viewBox="0 0 10 10"><circle cx="5" cy="5" r="4.4" fill="none" stroke="#333" stroke-width="0.9"/><path d="M3.4 2.8c.5 1.8 1.6 3.2 3.2 4.3" stroke="#333" stroke-width="1.2" fill="none"/></svg>(310) 555-0142</div>
      <div class="contact-line"><svg width="9" height="7" viewBox="0 0 9 7"><rect width="9" height="7" fill="#444"/><path d="M0 0L4.5 4L9 0" stroke="#eee" stroke-width=".8" fill="none"/></svg>dusty@velabrookproperties.com</div>
    </div>
    <div class="contact">
      <div class="contact-name">Owen Tu</div>
      <div class="contact-line"><svg width="10" height="10" viewBox="0 0 10 10"><circle cx="5" cy="5" r="4.4" fill="none" stroke="#333" stroke-width="0.9"/><path d="M3.4 2.8c.5 1.8 1.6 3.2 3.2 4.3" stroke="#333" stroke-width="1.2" fill="none"/></svg>(310) 555-0187</div>
      <div class="contact-line"><svg width="9" height="7" viewBox="0 0 9 7"><rect width="9" height="7" fill="#444"/><path d="M0 0L4.5 4L9 0" stroke="#eee" stroke-width=".8" fill="none"/></svg>owen@velabrookproperties.com</div>
    </div>
  </div>

  <div class="abs script script--front">Prestigious<br>&nbsp;Workplace</div>

  <svg class="abs footer" viewBox="0 0 548 52" aria-hidden="true">
    <defs>
      <linearGradient id="yellowFrontFoot" x1="0" y1="0" x2="1" y2="0">
        <stop offset="0" stop-color="#fbe48a"/><stop offset=".5" stop-color="#f3c01c"/><stop offset="1" stop-color="#f3c01c"/>
      </linearGradient>
    </defs>
    <path d="M0 12C180 2 380 0 548 6V52H0Z" fill="url(#yellowFrontFoot)"/>
    <path d="M0 12C180 2 380 0 548 6V2C380 -4 180 -2 0 8Z" fill="#bdbdbd"/>
  </svg>
  <div class="abs footer-phone" style="left:406px;top:729px"><svg width="13" height="13" viewBox="0 0 10 10"><circle cx="5" cy="5" r="4.4" fill="none" stroke="#222" stroke-width="0.9"/><path d="M3.4 2.8c.5 1.8 1.6 3.2 3.2 4.3" stroke="#222" stroke-width="1.2" fill="none"/></svg>(310) 555-0142</div>
  <div class="abs footer-small" style="left:22px;top:752px"><svg width="7" height="10" viewBox="0 0 7 10"><path d="M3.5 10C1 6.5 0 5 0 3.5a3.5 3.5 0 017 0C7 5 6 6.5 3.5 10Z" fill="#333"/><circle cx="3.5" cy="3.5" r="1.3" fill="#f3c01c"/></svg>5172 E Harlow Ave, Suite 414 West Hollywood, Ca. 90069</div>
  <div class="abs footer-small" style="left:368px;top:750px"><svg width="9" height="9" viewBox="0 0 10 10"><circle cx="5" cy="5" r="4.3" fill="none" stroke="#333"/><path d="M1 5h8M5 1c-2 2.5-2 5.5 0 8M5 1c2 2.5 2 5.5 0 8" stroke="#333" stroke-width=".7" fill="none"/></svg>www.velabrookproperties.com</div>
</section>

<section class="page page--back">
  <div class="abs amenities">
    <h2>BUILDING AMENITIES:</h2>
    <ul>
      <li><svg width="8" height="8" viewBox="0 0 8 8"><rect x=".5" y=".5" width="7" height="7" fill="none" stroke="#2c5aa0"/><path d="M1.8 4l1.6 1.6L7.5.8" stroke="#2c5aa0" stroke-width="1.2" fill="none"/></svg>Prestigious Ocean Front Location, with unobstructed Ocean Views</li>
      <li><svg width="8" height="8" viewBox="0 0 8 8"><rect x=".5" y=".5" width="7" height="7" fill="none" stroke="#2c5aa0"/><path d="M1.8 4l1.6 1.6L7.5.8" stroke="#2c5aa0" stroke-width="1.2" fill="none"/></svg>Suite provides Private Balconies and patios for Tenants exclusive use</li>
      <li><svg width="8" height="8" viewBox="0 0 8 8"><rect x=".5" y=".5" width="7" height="7" fill="none" stroke="#2c5aa0"/><path d="M1.8 4l1.6 1.6L7.5.8" stroke="#2c5aa0" stroke-width="1.2" fill="none"/></svg>Flexible Floorplans</li>
      <li><svg width="8" height="8" viewBox="0 0 8 8"><rect x=".5" y=".5" width="7" height="7" fill="none" stroke="#2c5aa0"/><path d="M1.8 4l1.6 1.6L7.5.8" stroke="#2c5aa0" stroke-width="1.2" fill="none"/></svg>Landlord to provide a Tenant Improvement Allowance to renovate the Space</li>
      <li><svg width="8" height="8" viewBox="0 0 8 8"><rect x=".5" y=".5" width="7" height="7" fill="none" stroke="#2c5aa0"/><path d="M1.8 4l1.6 1.6L7.5.8" stroke="#2c5aa0" stroke-width="1.2" fill="none"/></svg>Subterranean Parking</li>
      <li><svg width="8" height="8" viewBox="0 0 8 8"><rect x=".5" y=".5" width="7" height="7" fill="none" stroke="#2c5aa0"/><path d="M1.8 4l1.6 1.6L7.5.8" stroke="#2c5aa0" stroke-width="1.2" fill="none"/></svg>Recent Common area renovations</li>
      <li><svg width="8" height="8" viewBox="0 0 8 8"><rect x=".5" y=".5" width="7" height="7" fill="none" stroke="#2c5aa0"/><path d="M1.8 4l1.6 1.6L7.5.8" stroke="#2c5aa0" stroke-width="1.2" fill="none"/></svg>Kelp Haus, Tidal Oven and Ember Counter Restaurants are Tenants in the Building</li>
    </ul>
  </div>

  <div class="photo terrace-photo" role="img" aria-label="Photo of a shaded terrace with patio furniture and palm trees beyond"></div>
  <div class="photo lobby-photo" role="img" aria-label="Photo of the bright white lobby with a red runner and red abstract artwork"></div>
  <svg class="abs" style="left:0;top:376px" width="548" height="36" viewBox="0 0 548 36" aria-hidden="true">
    <path d="M0 18C160 6 400 4 548 12V36H0Z" fill="var(--page)"/>
    <path d="M0 18C160 6 400 4 548 12V16C400 10 160 12 0 24Z" fill="#2c2c2c"/>
  </svg>

  <div class="abs map" role="img" aria-label="Street map locating the building on Ocean Avenue near the beach and promenade"></div>
  <div class="abs beach-photo" role="img" aria-label="Photo of the beach and palm trees seen from a balcony"></div>

  <div class="abs brand" style="left:26px;top:628px;width:108px">
    <span class="brand-mark"></span>
    <span class="brand-name">VELABROOK<br>PROPERTIES</span>
  </div>

  <div class="abs script script--back">Bellwether Court</div>

  <div class="abs contact-panel" style="left:158px;top:660px;width:366px;height:58px">
    <div class="contact">
      <div class="contact-name">Dustin R. Hallorann</div>
      <div class="contact-line"><svg width="10" height="10" viewBox="0 0 10 10"><circle cx="5" cy="5" r="4.4" fill="none" stroke="#333" stroke-width="0.9"/><path d="M3.4 2.8c.5 1.8 1.6 3.2 3.2 4.3" stroke="#333" stroke-width="1.2" fill="none"/></svg>(310) 555-0142</div>
      <div class="contact-line"><svg width="9" height="7" viewBox="0 0 9 7"><rect width="9" height="7" fill="#444"/><path d="M0 0L4.5 4L9 0" stroke="#eee" stroke-width=".8" fill="none"/></svg>dusty@velabrookproperties.com</div>
    </div>
    <div class="contact">
      <div class="contact-name">Owen Tu</div>
      <div class="contact-line"><svg width="10" height="10" viewBox="0 0 10 10"><circle cx="5" cy="5" r="4.4" fill="none" stroke="#333" stroke-width="0.9"/><path d="M3.4 2.8c.5 1.8 1.6 3.2 3.2 4.3" stroke="#333" stroke-width="1.2" fill="none"/></svg>(310) 555-0187</div>
      <div class="contact-line"><svg width="9" height="7" viewBox="0 0 9 7"><rect width="9" height="7" fill="#444"/><path d="M0 0L4.5 4L9 0" stroke="#eee" stroke-width=".8" fill="none"/></svg>owen@velabrookproperties.com</div>
    </div>
  </div>

  <svg class="abs footer" viewBox="0 0 548 52" aria-hidden="true">
    <defs>
      <linearGradient id="yellowBackFoot" x1="0" y1="0" x2="1" y2="0">
        <stop offset="0" stop-color="#f3c01c"/><stop offset=".5" stop-color="#f3c01c"/><stop offset="1" stop-color="#fbe48a"/>
      </linearGradient>
    </defs>
    <path d="M0 6C170 0 370 2 548 12V52H0Z" fill="url(#yellowBackFoot)"/>
    <path d="M0 6C170 0 370 2 548 12V8C370 -2 170 -4 0 2Z" fill="#bdbdbd"/>
  </svg>
  <div class="abs footer-phone" style="left:20px;top:729px"><svg width="13" height="13" viewBox="0 0 10 10"><circle cx="5" cy="5" r="4.4" fill="none" stroke="#222" stroke-width="0.9"/><path d="M3.4 2.8c.5 1.8 1.6 3.2 3.2 4.3" stroke="#222" stroke-width="1.2" fill="none"/></svg>(310) 555-0142</div>
  <div class="abs footer-small" style="left:20px;top:750px"><svg width="9" height="9" viewBox="0 0 10 10"><circle cx="5" cy="5" r="4.3" fill="none" stroke="#333"/><path d="M1 5h8M5 1c-2 2.5-2 5.5 0 8M5 1c2 2.5 2 5.5 0 8" stroke="#333" stroke-width=".7" fill="none"/></svg>www.velabrookproperties.com</div>
  <div class="abs footer-small" style="left:266px;top:752px"><svg width="7" height="10" viewBox="0 0 7 10"><path d="M3.5 10C1 6.5 0 5 0 3.5a3.5 3.5 0 017 0C7 5 6 6.5 3.5 10Z" fill="#333"/><circle cx="3.5" cy="3.5" r="1.3" fill="#f3c01c"/></svg>5172 E Harlow Ave, Suite 414 West Hollywood, Ca. 90069</div>
</section>

</body>
</html>
```